Business Card Design Project - Small Bar

We would like a design for a business card for our new small bar in Melbourne. It is quite the 'hipster' bar and the card would need to reflect this in its design. We do have a logo which needs to be used in the card, tho how it is incorporated is up to you! :)

OK, the Bar currently has a common 'inner city' vibe, i.e. random artwork, older 30s/40's club furniture, grafitti murals on the walls, eclectic objects etc etc Current clientele would be described as "hipster", "urban professional" etc. How to describe... they are 30, have a good job but have beards, beanies and own vinyl records. :)

The card will be used to give to professional contacts and to bands/solo artists we come across to invite them to come play at our venue, so somehow I would like it to convey the image of 'professional' and 'funky' all in one. Difficult I know.

I have asked for some advice on making this brief clearer, so check back.

Thanks all in advance. :)
Updates

Sorry all

I've now been told that it is WEST MELBOURNE 3003. Apparently we are on the border and it is referred to by either west or north Melbourne, but it is definitely West Melbourne 3003.

Things you learn hey? :)

Target Market(s)

Hipsters, urbanites, the inner city crowd

Industry/Entity Type

Artists

Requirements
Must have
• Logo (JPG file attached)
Name of the bar "The Lantern & Otter"
Address - 742 Brindle St, North Melbourne, Victoria 3051
Names - Owen Partridge, Lewis Dunhurst
mobile. 0417265093 and 0456302714
Obviously we would need separate cards?
Nice to have
• Friendbook link
Friendbook 'like' icon
Should not have
• traditional designs. I am looking for something unique and funky. with FUNK! :)

```html
<!DOCTYPE html>
<html lang="en">
<head>
<meta charset="utf-8">
<title>The Lantern &amp; Otter — Business Cards</title>
<link href="https://fonts.googleapis.com/css2?family=Share+Tech&display=swap" rel="stylesheet">
<style>
  :root {
    --plum: #5c0040;
    --charcoal: #4a4a4a;
    --ink: #111111;
    --paper: #ffffff;
    --floor: #8c8c8c;
    --text-dark: #1a1a1a;
    --social: #3b5998;
  }
  * { margin: 0; padding: 0; box-sizing: border-box; }
  html, body { width: 1200px; height: 1200px; overflow: hidden; }
  body {
    background: var(--paper);
    font-family: "Share Tech", sans-serif;
    position: relative;
  }

  .hero {
    position: absolute;
    left: 0; top: 0;
    width: 1200px; height: 453px;
    background: var(--plum);
  }
  .hero__name {
    position: absolute;
    left: 0; right: 0; top: 200px;
    text-align: center;
    color: var(--paper);
    font-size: 52px;
    line-height: 1.05;
    letter-spacing: 2px;
  }

  .floor {
    position: absolute;
    left: 0; top: 988px;
    width: 1200px; height: 212px;
    background: var(--floor);
  }

  .card {
    position: absolute;
    top: 529px;
    width: 300px;
    height: 525px;
    overflow: hidden;
    box-shadow: 0 0 18px rgba(0,0,0,0.12);
  }
  .card--front { left: 69px; top: 535px; background: var(--ink); }
  .card--plum { left: 441px; background: var(--plum); }
  .card--grey { left: 815px; background: var(--charcoal); }

  .texture {
    position: absolute;
    inset: 0;
    background: radial-gradient(ellipse at 50% 55%, #2a2a2a 0%, #2a2a2a 38%, #7a7a7a 55%, #3a3a3a 80%, #0c0c0c 100%);
  }
  .spotlight {
    position: absolute;
    left: 50px; top: 130px;
    width: 210px; height: 270px;
    border-radius: 48% 52% 45% 55% / 50% 45% 55% 50%;
    background: radial-gradient(circle at 55% 45%, #3a3a3a 0%, #1e1e1e 100%);
  }
  .urban-art {
    position: absolute;
    right: 0; top: 0;
    width: 200px; height: 360px;
  }
  .card--plum .urban-art { background: linear-gradient(200deg, rgba(150,100,135,0.75) 0%, rgba(92,0,64,0) 75%); }
  .card--grey .urban-art { background: linear-gradient(200deg, rgba(160,160,160,0.75) 0%, rgba(74,74,74,0) 75%); }

  .brand {
    position: absolute;
    left: 0; right: 0;
    text-align: center;
    color: var(--paper);
    font-size: 30px;
    line-height: 1.05;
    letter-spacing: 1px;
  }
  .card--front .brand { top: 265px; }
  .card--plum .brand, .card--grey .brand { top: 215px; }

  .wave { position: absolute; left: 0; bottom: 0; width: 300px; height: 525px; }

  .contact {
    position: absolute;
    right: 30px;
    text-align: right;
    color: var(--text-dark);
    white-space: nowrap;
  }
  .contact__name { top: 392px; font-size: 24px; letter-spacing: 1.5px; }
  .contact__address { top: 430px; font-size: 13px; line-height: 18px; letter-spacing: 0.5px; }
  .contact__phone { top: 472px; font-size: 23px; letter-spacing: 2px; }
  .bar {
    position: absolute;
    right: 0; top: 406px;
    width: 23px; height: 6px;
  }
  .dot {
    position: absolute;
    right: 18px;
    width: 6px; height: 6px;
  }
  .card--plum .bar, .card--plum .dot { background: var(--plum); }
  .card--grey .bar, .card--grey .dot { background: var(--charcoal); }
  .dot--address { top: 437px; }
  .dot--phone { top: 482px; }
  .social {
    position: absolute;
    left: 26px; top: 480px;
    font-size: 13px;
    color: var(--text-dark);
    display: flex; align-items: center; gap: 5px;
  }
  .social__mark { width: 10px; height: 10px; background: var(--social); }
</style>
</head>
<body>
  <header class="hero">
    <div class="hero__name">The Lantern<br>&amp; Otter</div>
  </header>

  <div class="floor"></div>

  <section class="card card--front">
    <div class="texture" role="img" aria-label="Grunge halftone dot texture with ink splatters in grey and black"></div>
    <div class="spotlight"></div>
    <div class="brand">The Lantern<br>&amp; Otter</div>
  </section>

  <section class="card card--plum">
    <div class="urban-art" role="img" aria-label="Faded urban artwork of a building, swirls and splatters in plum tones"></div>
    <div class="brand">The Lantern<br>&amp; Otter</div>
    <svg class="wave" viewBox="0 0 300 525"><path d="M0,440 C80,392 150,372 220,362 C270,354 292,340 300,310 L300,525 L0,525 Z" fill="#ffffff"/></svg>
    <div class="contact contact__name">Owen Partridge</div><span class="bar"></span>
    <div class="contact contact__address">742 Brindle St, North Melbourne<br>Victoria 3051</div><span class="dot dot--address"></span>
    <div class="contact contact__phone">0417265093</div><span class="dot dot--phone"></span>
    <div class="social"><span class="social__mark"></span>Friendbook</div>
  </section>

  <section class="card card--grey">
    <div class="urban-art" role="img" aria-label="Faded urban artwork of a building, swirls and splatters in grey tones"></div>
    <div class="brand">The Lantern<br>&amp; Otter</div>
    <svg class="wave" viewBox="0 0 300 525"><path d="M0,440 C80,392 150,372 220,362 C270,354 292,340 300,310 L300,525 L0,525 Z" fill="#ffffff"/></svg>
    <div class="contact contact__name">Lewis Dunhurst</div><span class="bar"></span>
    <div class="contact contact__address">742 Brindle St, North Melbourne<br>Victoria 3051</div><span class="dot dot--address"></span>
    <div class="contact contact__phone">0456302714</div><span class="dot dot--phone"></span>
    <div class="social"><span class="social__mark"></span>Friendbook</div>
  </section>
</body>
</html>
```